Body therapist needs a business card

I need a card for my business which is teaching trainings in body therapy, the company is called Wexcombe Educational Group. I teach to massage therapists around Australia, South East Asia and the USA. I am attaching my logo which will guide you as to what colours I would like to have you consider. Please consult my website to find out more about what I do. www.corvantela.com.au

My name is Daniel Wexcombe. My phone number is (03) 9417 2608 or 0461753208. email is info@corvantela.com.au

```html
<!DOCTYPE html>
<html lang="en">
<head>
<meta charset="utf-8">
<title>Wexcombe Educational Group – Business Card</title>
<link href="https://fonts.googleapis.com/css2?family=Lato:wght@300;400;700&display=swap" rel="stylesheet">
<style>
  :root {
    --bg: #1c1c1c;
    --card: #2b2c2c;
    --card-deep: #252626;
    --lime: #c9d92a;
    --brown: #5e3020;
    --red: #b92025;
    --text: #e9e9e9;
    --muted: #bdbdbd;
    --rule: #6a6a6a;
  }
  * { box-sizing: border-box; margin: 0; padding: 0; }
  html, body { width: 1200px; height: 1108px; overflow: hidden; }
  body {
    background: var(--bg);
    font-family: "Lato", sans-serif;
    position: relative;
  }
  .card {
    position: absolute;
    top: 164px;
    width: 440px;
    height: 780px;
    border-radius: 22px;
    background: var(--card);
    overflow: hidden;
  }
  .card--front { left: 130px; }
  .card--back { left: 630px; }

  /* Front */
  .brand {
    position: absolute;
    top: 150px; left: 0; right: 0;
    display: flex; align-items: center; justify-content: center; gap: 14px;
  }
  .brand__dot {
    width: 34px; height: 34px; border-radius: 50%;
    background: var(--lime);
  }
  .brand__name {
    font-weight: 700; font-size: 38px; color: var(--lime);
    letter-spacing: 0.5px;
  }
  .identity {
    position: absolute; top: 330px; left: 0; right: 0; text-align: center;
  }
  .identity__name { font-weight: 700; font-size: 34px; color: var(--lime); }
  .identity__title { font-weight: 300; font-size: 21px; color: var(--muted); margin-top: 6px; }
  .divider {
    position: absolute; left: 70px; right: 70px; height: 1px; background: var(--rule);
  }
  .divider--icons { top: 430px; }
  .icons {
    position: absolute; top: 414px; left: 0; right: 0;
    display: flex; justify-content: center; gap: 6px;
  }
  .icons svg { background: var(--card); border-radius: 50%; }
  .contact {
    position: absolute; top: 466px; left: 0; right: 0; text-align: center;
    font-size: 20px; line-height: 33px; color: var(--text);
  }
  .divider--address { top: 582px; }
  .address {
    position: absolute; top: 604px; left: 0; right: 0; text-align: center;
    font-size: 20px; line-height: 30px; color: var(--text);
  }
  .address__company { color: var(--lime); font-weight: 700; font-size: 21px; }

  /* Back */
  .pattern {
    position: absolute; inset: 0;
    background: linear-gradient(180deg, #3a3b3b 0%, #313232 55%, var(--card-deep) 100%);
  }
  .back-brand {
    position: absolute; left: 0; right: 0; bottom: 150px;
    display: flex; align-items: center; justify-content: center; gap: 10px;
  }
  .back-brand__dot { width: 22px; height: 22px; border-radius: 50%; background: var(--lime); }
  .back-brand__name { font-weight: 700; font-size: 24px; color: var(--lime); }
</style>
</head>
<body>
  <section class="card card--front">
    <div class="brand">
      <span class="brand__dot"></span>
      <span class="brand__name">Wexcombe</span>
    </div>

    <div class="identity">
      <h1 class="identity__name">Daniel Wexcombe</h1>
      <p class="identity__title">Founder &amp; Trainer</p>
    </div>

    <div class="divider divider--icons"></div>
    <div class="icons">
      <svg class="icon icon--phone" width="32" height="32" viewBox="0 0 32 32" aria-label="Phone">
        <circle cx="16" cy="16" r="14" fill="var(--lime)"/>
        <path d="M11 9c1 0 2 2 2.5 3s-1 1.5-1 2.2c.6 1.7 2.4 3.5 4.3 4.3.7 0 1.2-1.5 2.2-1s3 1.5 3 2.5-1.5 3-3 3C13 23 9 19 9 13c0-2 1-4 2-4z" fill="var(--card)"/>
      </svg>
      <svg class="icon icon--mail" width="32" height="32" viewBox="0 0 32 32" aria-label="Email">
        <circle cx="16" cy="16" r="14" fill="var(--lime)"/>
        <rect x="8" y="11" width="16" height="11" fill="none" stroke="var(--card)" stroke-width="1.8"/>
        <path d="M8 11l8 6 8-6" fill="none" stroke="var(--card)" stroke-width="1.8"/>
      </svg>
      <svg class="icon icon--web" width="32" height="32" viewBox="0 0 32 32" aria-label="Website">
        <circle cx="16" cy="16" r="14" fill="var(--lime)"/>
        <circle cx="16" cy="16" r="8" fill="none" stroke="var(--card)" stroke-width="1.6"/>
        <ellipse cx="16" cy="16" rx="3.5" ry="8" fill="none" stroke="var(--card)" stroke-width="1.4"/>
        <path d="M8 16h16M9.5 12h13M9.5 20h13" stroke="var(--card)" stroke-width="1.3"/>
      </svg>
    </div>

    <div class="contact">
      <p>(03) 9417 2608</p>
      <p>info@corvantela.com.au</p>
      <p>www.corvantela.com.au</p>
    </div>

    <div class="divider divider--address"></div>
    <div class="address">
      <p class="address__company">Wexcombe Educational Group</p>
      <p>P.O. Box 2184 Ferndale North</p>
      <p>Victoria, 3147 Australia</p>
    </div>
  </section>

  <section class="card card--back">
    <div class="pattern" role="img" aria-label="Faint repeating circle pattern in dark grey tones"></div>
    <div class="back-brand">
      <span class="back-brand__dot"></span>
      <span class="back-brand__name">Wexcombe</span>
    </div>
  </section>
</body>
</html>
```